Willow Hex Teas needs 5 Cylinder Packaging Labels

I am looking for 5 variations of cylinder label designs for my herbal tea company, to use on eco-friendly matte black cardboard cylinder packaging.
Willow Hex Teas is launching soon and will have 3 wellness teas, as well as 2 ritual teas. All organic and eco-conscious.
Wellness: Driftleaf Blend (calming and soothing), Brightwick Tea (energetic and fresh) and Fern Cradle Tea (for women's wellbeing).
Ritual Teas: 'Lumen' (clear and focused, to prepare for meditation and ritual work) and 'Tessera' (energising and powerful, to use during ritual and magical workings).
I am looking for an earthy, herbal, yet also an antiqued mysterious look, to compliment the brand's brightwick. I am an brightwick worker and charge the herbal blends with intention for customers. I would like the packaging to promote a magical and witchy feel to an organic herbal brand.
I also love the idea of watercolour being used in the design, but this isn't a dealbreaker. I am very open to the designer's interpretation of my brand!
I would like to see each tea blend have a different colour to suit the type of tea (eg: Tessera ritual tea using purples, Lumen ritual tea using greens, fern cradle tea using pinks, brightwick tea using oranges, driftleaf blend using blues).
I would love to see some rich, jewel tones incorporated in this product design!
I have added a few inspiration photos to this brief, as well as a logo mock-up which I would like used in the design. I would also like to see the brand name ‘Willow Hex Teas’ with this logo.
Updates
Designs look the same
Target Market(s)
My ideal customer is spiritually connected (yoga, meditation, witches, healers, etc), interested in holistic wellness and environmentally driven.
Industry/Entity Type
Tea, Holistic Wellness
Requirements
Must have
- 5 variations of a cohesive herbal tea brand label. I will need to include ingredients, brewing instructions and product weight on the label. I would also like to see indications that the packaging is eco-friendly and made in Australia.
Nice to have
- I would like to see some deep jewel tones incorporated in the label designs, with perhaps some gold for the ritual teas, to have them stand out as our luxury range.

```html
<!DOCTYPE html>
<html lang="en">
<head>
<meta charset="utf-8">
<title>Willow Hex Teas – Cylinder Labels</title>
<link rel="stylesheet" href="https://fonts.googleapis.com/css2?family=Cormorant+Garamond:wght@500;700&family=Cinzel:wght@400;600&family=Great+Vibes&display=swap">
<style>
  :root {
    --page: #ffffff;
    --ink: #ffffff;
    --rule: rgba(255,255,255,.55);
    --night: #05070a;
    --blue-hi: #22bdf0; --blue-mid: #0c4f86; --blue-deep: #071726;
    --orange-hi: #f39a1c; --orange-mid: #9a3d12; --orange-deep: #1d0c06;
    --pink-hi: #e8489f; --pink-mid: #8a1f6e; --pink-deep: #1c0617;
    --teal-hi: #1f9a84; --teal-mid: #0d5a5e; --teal-deep: #061a1c;
    --violet-hi: #6a4cb0; --violet-mid: #35286e; --violet-deep: #0c0a1e;
    --gold-a: #b8923e; --gold-b: #f0dca0; --gold-c: #c9a34f;
    --silver-a: #8d8d8d; --silver-b: #f4f4f4; --silver-c: #a9a9a9;
  }
  * { margin: 0; padding: 0; box-sizing: border-box; }
  html, body { width: 1200px; height: 1200px; overflow: hidden; background: var(--page); }
  .sheet { position: relative; width: 1200px; height: 1200px; }

  .label { position: absolute; width: 302px; height: 560px; overflow: hidden; color: var(--ink); background: var(--night); }
  .label--r1 { top: 42px; }
  .label--r2 { top: 621px; }
  .label--c1 { left: 126px; }
  .label--c2 { left: 477px; }
  .label--c3 { left: 817px; }

  .label__band { position: absolute; left: 0; top: 0; width: 100%; height: 98px; }
  .label__seal { position: absolute; left: 123px; top: 22px; width: 56px; height: 56px; border-radius: 50%;
    background: radial-gradient(circle at 40% 35%, var(--seal-hi), var(--seal-lo)); border: 2px solid rgba(255,255,255,.85); }

  .label__wash { position: absolute; left: 0; top: 98px; width: 100%; height: 462px; }

  .label__frame { position: absolute; left: 36px; right: 36px; top: 144px; bottom: 28px; border: 1px solid var(--rule); }

  .label__range { position: absolute; top: 150px; width: 100%; text-align: center;
    font-family: "Great Vibes", cursive; font-size: 30px; line-height: 1; }
  .label__brand { position: absolute; top: 238px; width: 100%; text-align: center;
    font-family: "Cormorant Garamond", serif; font-weight: 500; font-size: 36px; line-height: 1; letter-spacing: .5px; }
  .label__brand span { display: block; }
  .label__brand-mark { display: inline-block; width: 10px; height: 10px; border-radius: 50%; background: var(--ink); margin-bottom: 12px; }

  .info { position: absolute; left: 52px; right: 42px; top: 398px; height: 57px;
    border-top: 1px solid var(--rule); border-bottom: 1px solid var(--rule); }
  .info__split { position: absolute; left: 120px; top: 0; bottom: 0; border-left: 1px solid var(--rule); }
  .info__mid { position: absolute; left: 0; right: 0; top: 36px; border-top: 1px solid var(--rule); }
  .info__name { position: absolute; left: 0; width: 120px; top: 6px; text-align: center;
    font-family: "Cormorant Garamond", serif; font-weight: 700; font-size: 20px; letter-spacing: 1px; white-space: nowrap; }
  .info__note { position: absolute; left: 132px; top: 8px; font-family: "Cinzel", serif; font-size: 9px; line-height: 10px; letter-spacing: .8px; }
  .info__origin { position: absolute; left: 0; width: 120px; top: 41px; text-align: center; font-family: "Cinzel", serif; font-size: 6.5px; letter-spacing: .5px; }
  .info__weight { position: absolute; left: 120px; right: 0; top: 37px; text-align: center; font-family: "Cormorant Garamond", serif; font-weight: 700; font-size: 15px; }

  .brew { position: absolute; left: 46px; right: 46px; top: 465px; text-align: center;
    font-family: "Cinzel", serif; font-size: 7px; line-height: 10px; letter-spacing: .3px; }
  .brew b { font-weight: 600; }

  .theme-blue .label__band { background: linear-gradient(100deg, #16a9e2, var(--blue-hi) 40%, #8fe0ff 52%, #1498d8 70%, #2ac2f2); }
  .theme-blue .label__wash { background:
      linear-gradient(to right, transparent 45%, rgba(0,0,0,.85) 95%),
      linear-gradient(170deg, var(--night) 8%, var(--blue-mid) 35%, var(--blue-deep) 55%, var(--blue-mid) 70%, var(--blue-hi) 95%); }
  .theme-blue { --seal-hi: #3fd0c8; --seal-lo: #0a3d52; }

  .theme-orange .label__band { background: linear-gradient(100deg, #e8701a, var(--orange-hi) 40%, #ffd060 52%, #f07a18 70%, #f59a22); }
  .theme-orange .label__wash { background:
      linear-gradient(to right, transparent 45%, rgba(0,0,0,.8) 95%),
      linear-gradient(170deg, var(--night) 8%, var(--orange-mid) 35%, var(--orange-deep) 55%, #b8501a 72%, var(--orange-hi) 95%); }
  .theme-orange { --seal-hi: #ffd23a; --seal-lo: #b83a10; }

  .theme-pink .label__band { background: linear-gradient(100deg, #e070b8, var(--pink-hi) 40%, #ffb0dc 52%, #e04aa4 70%, #ea5cae); }
  .theme-pink .label__wash { background:
      linear-gradient(to right, transparent 50%, rgba(0,0,0,.75) 95%),
      linear-gradient(170deg, var(--night) 8%, var(--pink-mid) 35%, var(--pink-deep) 55%, #b02c88 72%, var(--pink-hi) 95%); }
  .theme-pink { --seal-hi: #c8a8e8; --seal-lo: #6a2a7e; }

  .theme-teal .label__band { background: linear-gradient(100deg, var(--gold-a), var(--gold-b) 45%, var(--gold-c) 70%, #e6c97e); }
  .theme-teal .label__wash { background:
      linear-gradient(to right, transparent 50%, rgba(0,0,0,.75) 95%),
      linear-gradient(170deg, var(--night) 8%, var(--teal-mid) 35%, var(--teal-deep) 55%, var(--teal-mid) 72%, var(--teal-hi) 95%); }
  .theme-teal { --seal-hi: #3fd6e0; --seal-lo: #0d3f6a; }

  .theme-violet .label__band { background: linear-gradient(100deg, var(--gold-a), var(--gold-b) 45%, var(--gold-c) 70%, #e6c97e); }
  .theme-violet .label__wash { background:
      linear-gradient(to right, transparent 50%, rgba(0,0,0,.75) 95%),
      linear-gradient(170deg, var(--night) 8%, var(--violet-mid) 35%, var(--violet-deep) 55%, var(--violet-mid) 72%, var(--violet-hi) 95%); }
  .theme-violet { --seal-hi: #3fd6e0; --seal-lo: #0d3f6a; }

  .theme-silver .label__band { background: linear-gradient(120deg, var(--silver-a), var(--silver-b) 35%, var(--silver-c) 55%, var(--silver-b) 80%, #bdbdbd); }
  .theme-silver .label__wash { background:
      linear-gradient(to right, transparent 50%, rgba(0,0,0,.75) 95%),
      linear-gradient(170deg, var(--night) 8%, var(--pink-mid) 35%, var(--pink-deep) 55%, #b02c88 72%, var(--pink-hi) 95%); }
  .theme-silver { --seal-hi: #b890f0; --seal-lo: #2a2a7e; }
</style>
</head>
<body>
<main class="sheet">

  <section class="label label--r1 label--c1 theme-blue">
    <div class="label__band" role="img" aria-label="Metallic blue band with repeating brand name pattern"></div>
    <div class="label__seal" role="img" aria-label="Eco-friendly recyclable seal"></div>
    <div class="label__wash" role="img" aria-label="Blue and black watercolour wash with gold splatter"></div>
    <div class="label__frame"></div>
    <p class="label__range">wellness</p>
    <h2 class="label__brand"><span class="label__brand-mark"></span><span>Willow Hex</span><span>Teas</span></h2>
    <div class="info">
      <div class="info__split"></div><div class="info__mid"></div>
      <p class="info__name">driftleaf</p>
      <p class="info__note">CALMING &amp;<br>SOOTHING</p>
      <p class="info__origin">MADE IN AUSTRALIA</p>
      <p class="info__weight">2.oz</p>
    </div>
    <p class="brew"><b>BREWING INSTRUCTIONS:</b> LOREM IPSUM DOLOR SIT AMET, CONSECTETUER ADIPISCING ELIT, SED DIAM. LOREM IPSUM DOLOR SIT AMET, CONSECTETUER ADIPISCING ELIT, SED DIAM.</p>
  </section>

  <section class="label label--r1 label--c2 theme-orange">
    <div class="label__band" role="img" aria-label="Metallic orange band with repeating brand name pattern"></div>
    <div class="label__seal" role="img" aria-label="Eco-friendly recyclable seal"></div>
    <div class="label__wash" role="img" aria-label="Orange and black watercolour wash with gold splatter"></div>
    <div class="label__frame"></div>
    <p class="label__range">wellness</p>
    <h2 class="label__brand"><span class="label__brand-mark"></span><span>Willow Hex</span><span>Teas</span></h2>
    <div class="info">
      <div class="info__split"></div><div class="info__mid"></div>
      <p class="info__name">brightwick</p>
      <p class="info__note">ENERGETIC<br>&amp; FRESH</p>
      <p class="info__origin">MADE IN AUSTRALIA</p>
      <p class="info__weight">2.oz</p>
    </div>
    <p class="brew"><b>BREWING INSTRUCTIONS:</b> LOREM IPSUM DOLOR SIT AMET, CONSECTETUER ADIPISCING ELIT, SED DIAM. LOREM IPSUM DOLOR SIT AMET, CONSECTETUER ADIPISCING ELIT, SED DIAM.</p>
  </section>

  <section class="label label--r1 label--c3 theme-pink">
    <div class="label__band" role="img" aria-label="Metallic pink band with repeating brand name pattern"></div>
    <div class="label__seal" role="img" aria-label="Eco-friendly recyclable seal"></div>
    <div class="label__wash" role="img" aria-label="Pink and black watercolour wash with gold splatter"></div>
    <div class="label__frame"></div>
    <p class="label__range">wellness</p>
    <h2 class="label__brand"><span class="label__brand-mark"></span><span>Willow Hex</span><span>Teas</span></h2>
    <div class="info">
      <div class="info__split"></div><div class="info__mid"></div>
      <p class="info__name">fern cradle</p>
      <p class="info__note">FEMANINE<br>WELLBEING</p>
      <p class="info__origin">MADE IN AUSTRALIA</p>
      <p class="info__weight">2.oz</p>
    </div>
    <p class="brew"><b>BREWING INSTRUCTIONS:</b> LOREM IPSUM DOLOR SIT AMET, CONSECTETUER ADIPISCING ELIT, SED DIAM. LOREM IPSUM DOLOR SIT AMET, CONSECTETUER ADIPISCING ELIT, SED DIAM.</p>
  </section>

  <section class="label label--r2 label--c1 theme-teal">
    <div class="label__band" role="img" aria-label="Metallic gold band with repeating brand name pattern"></div>
    <div class="label__seal" role="img" aria-label="Eco-friendly recyclable seal"></div>
    <div class="label__wash" role="img" aria-label="Teal green and black watercolour wash with gold splatter"></div>
    <div class="label__frame"></div>
    <p class="label__range">ritual</p>
    <h2 class="label__brand"><span class="label__brand-mark"></span><span>Willow Hex</span><span>Teas</span></h2>
    <div class="info">
      <div class="info__split"></div><div class="info__mid"></div>
      <p class="info__name">lumen</p>
      <p class="info__note">FRESH &amp;<br>FOCUSED</p>
      <p class="info__origin">MADE IN AUSTRALIA</p>
      <p class="info__weight">2.oz</p>
    </div>
    <p class="brew"><b>BREWING INSTRUCTIONS:</b> LOREM IPSUM DOLOR SIT AMET, CONSECTETUER ADIPISCING ELIT, SED DIAM. LOREM IPSUM DOLOR SIT AMET, CONSECTETUER ADIPISCING ELIT, SED DIAM.</p>
  </section>

  <section class="label label--r2 label--c2 theme-violet">
    <div class="label__band" role="img" aria-label="Metallic gold band with repeating brand name pattern"></div>
    <div class="label__seal" role="img" aria-label="Eco-friendly recyclable seal"></div>
    <div class="label__wash" role="img" aria-label="Purple and black watercolour wash with gold splatter"></div>
    <div class="label__frame"></div>
    <p class="label__range">ritual</p>
    <h2 class="label__brand"><span class="label__brand-mark"></span><span>Willow Hex</span><span>Teas</span></h2>
    <div class="info">
      <div class="info__split"></div><div class="info__mid"></div>
      <p class="info__name">tessera</p>
      <p class="info__note">ENERGISING &amp;<br>POWERFUL</p>
      <p class="info__origin">MADE IN AUSTRALIA</p>
      <p class="info__weight">2.oz</p>
    </div>
    <p class="brew"><b>BREWING INSTRUCTIONS:</b> LOREM IPSUM DOLOR SIT AMET, CONSECTETUER ADIPISCING ELIT, SED DIAM. LOREM IPSUM DOLOR SIT AMET, CONSECTETUER ADIPISCING ELIT, SED DIAM.</p>
  </section>

  <section class="label label--r2 label--c3 theme-silver">
    <div class="label__band" role="img" aria-label="Metallic silver band with repeating brand name pattern"></div>
    <div class="label__seal" role="img" aria-label="Eco-friendly recyclable seal"></div>
    <div class="label__wash" role="img" aria-label="Pink and black watercolour wash with gold splatter"></div>
    <div class="label__frame"></div>
    <p class="label__range">wellness</p>
    <h2 class="label__brand"><span class="label__brand-mark"></span><span>Willow Hex</span><span>Teas</span></h2>
    <div class="info">
      <div class="info__split"></div><div class="info__mid"></div>
      <p class="info__name">fern cradle</p>
      <p class="info__note">FEMANINE<br>WELLBEING</p>
      <p class="info__origin">MADE IN AUSTRALIA</p>
      <p class="info__weight">2.oz</p>
    </div>
    <p class="brew"><b>BREWING INSTRUCTIONS:</b> LOREM IPSUM DOLOR SIT AMET, CONSECTETUER ADIPISCING ELIT, SED DIAM. LOREM IPSUM DOLOR SIT AMET, CONSECTETUER ADIPISCING ELIT, SED DIAM.</p>
  </section>

</main>
</body>
</html>
```